Tidewell show guide

I need to design a one page 7x10 pdf that will be printed. It will include our logo and the following text:

#1 Disaster Mitigation Lead Platform

We generated over 60 million in
revenue last year fo our contractors.

Leads types:
-Water Damage
-Fire Damage
-Mold Remediation
-Biohazard
-Plumbing
-Carpet Cleaning

Exclusive leads
No monthly fees
Only pay for valid leads

Stop by booth 814 to get to your cut!

Target Market(s)

Home service contractors

Colors
9bcb3b
0255a3

Requirements
Must have
• our logo and text
Should not have
• any clutter

```html
<!DOCTYPE html>
<html lang="en">
<head>
<meta charset="utf-8">
<title>Tidewell show guide</title>
<link rel="stylesheet" href="https://fonts.googleapis.com/css2?family=Bebas+Neue&family=Montserrat:wght@700;800&display=swap">
<style>
  :root {
    --blue: #0f61b6;
    --blue-deep: #0255a3;
    --blue-light: #b8d2ef;
    --green: #16a63c;
    --paper: #f5f6f7;
    --white: #ffffff;
  }
  * { margin: 0; padding: 0; box-sizing: border-box; }
  html, body { width: 869px; height: 1200px; overflow: hidden; background: var(--paper); }
  .flyer { position: relative; width: 869px; height: 1200px; overflow: hidden; background: var(--paper); font-family: "Montserrat", Arial, sans-serif; }
  .geometry { position: absolute; inset: 0; }
  .brand { position: absolute; left: 496px; top: 50px; display: flex; align-items: center; gap: 12px; white-space: nowrap; }
  .brand-dot { width: 62px; height: 62px; border: 6px solid var(--green); border-radius: 50%; flex: none; }
  .brand-name { font-size: 21px; font-weight: 700; letter-spacing: 2px; color: var(--green); white-space: nowrap; }
  .title { position: absolute; right: 50px; top: 172px; text-align: right; }
  .title-main { font-family: "Bebas Neue", "Arial Narrow", sans-serif; font-size: 112px; line-height: 0.8; color: var(--blue-deep); letter-spacing: -1px; }
  .title-sub { font-size: 19px; font-weight: 800; color: var(--green); margin-top: 4px; white-space: nowrap; }
  .claim { position: absolute; right: 50px; top: 586px; text-align: right; white-space: nowrap; }
  .claim-main { font-family: "Bebas Neue", "Arial Narrow", sans-serif; font-size: 61px; line-height: 0.9; color: var(--blue-deep); }
  .claim-sub { font-size: 24.5px; font-weight: 800; color: var(--green); letter-spacing: -0.6px; margin-top: 2px; }
  .label { position: absolute; color: var(--green); font-weight: 700; text-align: center; white-space: nowrap; }
  .label-heading { left: 289px; top: 741px; width: 291px; height: 32px; line-height: 32px; font-size: 19px; }
  .label-pill { top: 979px; height: 24px; line-height: 24px; font-size: 15.5px; }
  .lead-type { position: absolute; top: 915px; width: 140px; margin-left: -70px; text-align: center; color: var(--white); font-size: 10px; font-weight: 800; }
  .footer-call { position: absolute; left: 0; right: 0; top: 1126px; text-align: center; font-size: 32px; font-weight: 800; color: var(--green); letter-spacing: -0.8px; white-space: nowrap; }
</style>
</head>
<body>
<main class="flyer">
  <svg class="geometry" width="869" height="1200" viewBox="0 0 869 1200">
    <defs>
      <linearGradient id="storm" x1="0" y1="0" x2="0" y2="1">
        <stop offset="0" stop-color="#2a2722"/>
        <stop offset="0.2" stop-color="#a48f74"/>
        <stop offset="0.4" stop-color="#3b342c"/>
        <stop offset="0.62" stop-color="#8a6d52"/>
        <stop offset="0.78" stop-color="#27476b"/>
        <stop offset="1" stop-color="#1a2f4d"/>
      </linearGradient>
    </defs>
    <polygon class="photo" role="img" aria-label="Open cupped hands rising from a stormy sea under dark clouds" points="0,0 469,0 469,252 0,760" fill="url(#storm)"/>
    <polyline class="photo-frame" points="0,49 443,49 443,291 0,799" fill="none" stroke="var(--green)" stroke-width="4"/>

    <polygon points="526,348 621,348 572,427 477,427" fill="var(--blue)"/>
    <polygon points="655,331 697,331 656,376 614,376" fill="var(--green)"/>
    <polygon points="536,513 869,513 869,540 510,540" fill="var(--blue-light)"/>
    <polygon points="599,393 869,393 869,511 502,511" fill="var(--blue)"/>
    <polyline points="869,405 606,405 520,500 869,500" fill="none" stroke="#3a83cf" stroke-width="1.5"/>
    <polyline points="869,418 616,418 540,488 869,488" fill="none" stroke="#2c77c6" stroke-width="1.2"/>

    <path class="panel" d="M121,700 H869 V1070 Q869,1096 843,1096 H26 Q0,1096 0,1070 V821 Z" fill="var(--blue)"/>

    <g fill="none" stroke="var(--white)" stroke-width="1.2" stroke-dasharray="4 3">
      <path d="M94,841 V756 H289 M580,756 H771 V841"/>
      <path d="M230,841 V756 M374,841 V773 M519,841 V756 M639,841 V756"/>
      <path d="M248,991 H310 M509,991 H564"/>
    </g>
    <g fill="var(--white)">
      <polygon points="289,757 303,741 566,741 580,757 566,773 303,773"/>
      <polygon points="49,991 59,979 238,979 248,991 238,1003 59,1003"/>
      <polygon points="310,991 320,979 499,979 509,991 499,1003 320,1003"/>
      <polygon points="564,991 574,979 810,979 820,991 810,1003 574,1003"/>
    </g>

    <g class="lead-icons" fill="none" stroke="var(--white)">
      <g transform="translate(94,873)"><circle r="32" stroke-width="3"/><circle r="27" fill="var(--white)" stroke="none"/></g>
      <g transform="translate(230,873)"><circle r="32" stroke-width="3"/><circle r="27" fill="var(--white)" stroke="none"/></g>
      <g transform="translate(374,873)"><circle r="32" stroke-width="3"/><circle r="27" fill="var(--white)" stroke="none"/></g>
      <g transform="translate(519,873)"><circle r="32" stroke-width="3"/><circle r="27" fill="var(--white)" stroke="none"/></g>
      <g transform="translate(639,873)"><circle r="32" stroke-width="3"/><circle r="27" fill="var(--white)" stroke="none"/></g>
      <g transform="translate(771,873)"><circle r="32" stroke-width="3"/><circle r="27" fill="var(--white)" stroke="none"/></g>
    </g>
    <g fill="var(--blue)" stroke="var(--blue)" stroke-width="2.5" stroke-linecap="round" stroke-linejoin="round">
      <g transform="translate(94,873)"><path d="M-14,-2 L0,-14 L14,-2 V6 H-14 Z" fill="none"/><path d="M-16,10 q4,-4 8,0 t8,0 t8,0 t8,0" fill="none"/></g>
      <g transform="translate(230,873)"><path d="M-4,-2 L8,-13 L18,-2 V12 H-4" fill="none"/><path d="M-16,12 q-4,-10 4,-18 q0,8 5,10 q2,-5 -1,-9 q10,6 6,17 Z"/></g>
      <g transform="translate(374,873)"><circle cx="4" cy="-4" r="11" fill="none"/><rect x="-16" y="-2" width="12" height="12" rx="3"/><circle cx="6" cy="-4" r="4" fill="none"/></g>
      <g transform="translate(519,873)" fill="none"><circle cy="-7" r="8"/><circle cx="-8" cy="6" r="8"/><circle cx="8" cy="6" r="8"/><circle r="3" fill="var(--blue)"/></g>
      <g transform="translate(639,873)" fill="none"><path d="M-14,14 V-2 Q-14,-8 -8,-8 H8 V-13 M2,-13 H14 M8,-8 V-2"/><circle cx="8" cy="6" r="1.5" fill="var(--blue)"/></g>
      <g transform="translate(771,873)"><circle cx="-6" cy="-14" r="4"/><path d="M-6,-9 V4 L-10,16 M-6,4 L-1,16 M-6,-6 L6,4" fill="none"/><rect x="4" y="4" width="10" height="6" rx="2"/><circle cx="12" cy="14" r="2.5"/></g>
    </g>

    <g class="benefit-icons" fill="var(--white)">
      <g transform="translate(149,1042)">
        <circle cx="-12" cy="-12" r="8"/><path d="M-28,24 Q-28,-2 -12,-2 Q4,-2 4,24 Z"/>
        <circle cx="6" cy="-6" r="6"/><path d="M-4,24 Q-4,3 6,3 Q16,3 16,24 Z"/>
        <circle cx="20" cy="-2" r="5"/><path d="M11,24 Q11,6 20,6 Q29,6 29,24 Z"/>
      </g>
      <g transform="translate(410,1042)">
        <ellipse cx="0" cy="14" rx="18" ry="6"/><ellipse cx="0" cy="6" rx="18" ry="6" stroke="var(--blue)" stroke-width="2"/>
        <ellipse cx="0" cy="-2" rx="18" ry="6" stroke="var(--blue)" stroke-width="2"/>
        <circle cx="0" cy="-14" r="13" stroke="var(--blue)" stroke-width="2"/>
        <text x="0" y="-9" text-anchor="middle" font-family="Montserrat, sans-serif" font-weight="800" font-size="15" fill="var(--blue)">$</text>
      </g>
      <g transform="translate(692,1042)">
        <rect x="-14" y="-24" width="24" height="18" rx="3" transform="rotate(-15)"/>
        <rect x="-10" y="-6" width="30" height="22" rx="3" stroke="var(--blue)" stroke-width="2"/>
        <rect x="-10" y="0" width="30" height="4" fill="var(--blue)"/>
      </g>
    </g>
  </svg>

  <header class="brand">
    <span class="brand-dot"></span>
    <span class="brand-name">NORTHLINE LEADS</span>
  </header>

  <section class="title">
    <h1 class="title-main">DISASTER</h1>
    <p class="title-sub">MITIGATION LEAD PLATFORM</p>
  </section>

  <section class="claim">
    <p class="claim-main">WE GENERATED OVER 60 MILLION IN</p>
    <p class="claim-sub">REVENUE LAST YEAR FO OUR CONTRACTORS</p>
  </section>

  <p class="label label-heading">ESTATE DISTRIBUTION</p>
  <p class="lead-type" style="left:94px">WATER DAMAGE</p>
  <p class="lead-type" style="left:230px">FIRE DAMAGE</p>
  <p class="lead-type" style="left:374px">MOLD REMEDIATION</p>
  <p class="lead-type" style="left:519px">BIOHAZARD</p>
  <p class="lead-type" style="left:639px">PLUMBING</p>
  <p class="lead-type" style="left:771px">CARPET CLEANING</p>

  <p class="label label-pill" style="left:49px;width:199px">EXCLUSIVE LEADS</p>
  <p class="label label-pill" style="left:310px;width:199px">NO MONTHLY FEES</p>
  <p class="label label-pill" style="left:564px;width:256px">ONLY PAY FOR VALID LEADS</p>

  <p class="footer-call">STOP BY BOOTH 814 TO GET TO YOUR CUT!</p>
</main>
</body>
</html>
```